Printing company needs website!

A printing company would like a new professional website (made with wix). Now they don't have a website, but they want a unique, beautiful, clear site. Of course they provide the content themselves, we are now looking for the beautiful design with some mockups. You can see several of their projects on their instagram & facebook.
Www.kwelmast.com/brimvelt and https://www.fotoravel.com/brimvelt.be/ logos are attached.

```html
<!DOCTYPE html>
<html lang="nl">
<head>
<meta charset="utf-8">
<title>Brimvelt – waar alles brimvelt is</title>
<link href="https://fonts.googleapis.com/css2?family=Outfit:wght@300;400;500;600&display=swap" rel="stylesheet">
<style>
:root{
  --teal:#4cc2b0;
  --yellow:#f5cf1d;
  --blue:#16b4e0;
  --lime:#c2cc4e;
  --ink:#111111;
  --dark:#252223;
  --grey:#f1f1f1;
  --muted:#8a8a8a;
  --white:#ffffff;
}
*{margin:0;padding:0;box-sizing:border-box}
html,body{width:1200px;height:4399px;overflow:hidden}
body{font-family:"Outfit",sans-serif;color:var(--ink);background:var(--white);position:relative}
.abs{position:absolute}
.center{left:0;width:1200px;text-align:center}

/* header + hero */
.hero{left:0;top:0;width:1200px;height:1000px;
  background:linear-gradient(120deg,#2a1a22 0%,#8c2333 25%,#c9672b 45%,#3a6aa0 65%,#5b3a86 80%,#1b1b1b 100%)}
.hero-shade{left:0;top:0;width:1200px;height:1000px;background:linear-gradient(180deg,rgba(0,0,0,.92) 0,rgba(0,0,0,.35) 220px,rgba(0,0,0,.25) 100%)}
.brand{font-weight:500;color:var(--white);letter-spacing:.5px}
.brand-top{left:42px;top:44px;font-size:48px;line-height:1}
.brand-top small{display:block;font-size:13px;color:var(--teal);font-weight:300;margin-top:4px;padding-left:150px}
.call{right:72px;top:30px;font-size:22px;color:var(--yellow);font-weight:500;display:flex;align-items:center;gap:8px}
.nav{right:70px;top:80px;display:flex;gap:38px;font-size:16px;color:#cfcfcf;font-weight:300}
.nav .on{color:var(--teal);font-weight:500}
.hero-title{top:448px;font-size:86px;font-weight:500;color:var(--white);line-height:1}
.hero-tag{top:546px;font-size:36px;font-weight:300;color:var(--teal)}

/* services */
h2{font-weight:500;font-size:44px;line-height:1.1}
.lede{font-size:16px;font-weight:300;line-height:20px;color:#444;width:790px;left:205px;text-align:center}
.svc{width:290px;text-align:center}
.svc .ico{width:96px;height:96px;border-radius:50%;margin:0 auto;display:flex;align-items:center;justify-content:center}
.svc h3{font-size:22px;font-weight:400;margin-top:22px}
.svc p{font-size:14px;font-weight:300;color:var(--muted);line-height:17px;margin-top:16px;padding:0 12px}

/* about */
.about{left:0;top:1376px;width:1200px;height:672px;overflow:hidden}
.about h2{color:var(--white);left:118px;top:208px}
.about p{left:118px;width:486px;color:var(--white);font-size:16px;font-weight:300;line-height:18.5px}
.btn{display:flex;align-items:center;justify-content:center;border-radius:24px;font-weight:500;font-size:17px;letter-spacing:.5px}
.btn-blue{left:118px;top:490px;width:160px;height:48px;background:var(--blue);color:var(--white)}

/* works */
.card{top:2351px;width:229px;height:307px;border-radius:12px}
.arrow{top:2486px}

/* testimonial */
.testi{left:0;top:2868px;width:1200px;height:447px;background:var(--grey)}
.person{left:85px;top:2842px;width:333px;height:473px;background:linear-gradient(180deg,#d9d9d9,#7d7f84 60%,#5c5e63)}
.t-name{left:519px;top:2990px;font-size:23px;color:var(--teal);font-weight:400;letter-spacing:.5px}
.t-role{left:519px;top:3022px;font-size:12px;color:var(--muted);letter-spacing:1px}
.t-quote{left:517px;top:3058px;width:500px;font-size:20px;font-style:italic;font-weight:300;line-height:26px;color:#333}

/* cta */
.cta-bg{left:0;top:3397px;width:1200px;height:520px;background:linear-gradient(180deg,#fff 0,#fff 52%,#f4e9ef 65%,#f0d6a3 75%,#f2a29a 85%,#9fcbe6 100%)}
.cta-title{top:3500px;font-size:42px;font-weight:500;line-height:55px}
.btn-teal{left:471px;top:3653px;width:258px;height:40px;background:var(--teal);color:var(--white);font-size:17px}

/* footer */
.foot-brand{left:179px;top:4000px;font-size:50px;line-height:1}
.foot-brand small{display:block;font-size:13px;color:var(--teal);font-weight:300;padding-left:145px;margin-top:4px}
.foot-text{left:180px;top:4112px;width:322px;text-align:center;color:#bbb;font-size:13.5px;line-height:18px;font-weight:300}
.social{top:4190px;width:48px;height:48px;border-radius:50%;border:2px solid var(--yellow)}
.f-head{left:558px;top:3986px;color:var(--white);font-size:24px;font-weight:400}
.field{border:1px solid #bdbdbd;border-radius:22px;color:#ddd;font-size:13px;padding:0 14px;display:flex;align-items:center}
.field.msg{align-items:flex-start;padding-top:16px;border-radius:24px}
.submit{left:794px;top:4144px;width:256px;height:43px;background:var(--teal);color:var(--white);font-size:17px}
.f-info{top:4242px;font-size:17px;color:var(--yellow);display:flex;align-items:center;gap:8px}
.copy{top:4318px;color:#ccc;font-size:13px;font-weight:300}
.stripe{left:0;top:4381px;width:1200px;height:18px;background:linear-gradient(90deg,var(--teal) 0 30%,var(--yellow) 30% 45%,var(--blue) 45% 100%)}
</style>
</head>
<body>

<!-- HERO -->
<div class="abs hero" role="img" aria-label="Close-up photo of a hand holding a pencil over an open colour swatch fan"></div>
<div class="abs hero-shade"></div>

<div class="abs brand brand-top">Brimvelt<small>waar alles brimvelt is</small></div>
<div class="abs call">
  <svg width="24" height="24" viewBox="0 0 24 24"><circle cx="12" cy="12" r="12" fill="var(--yellow)"/><path d="M8 6.5l2 .3.8 3-1.3 1a7 7 0 003.7 3.7l1-1.3 3 .8.3 2c-.2.8-1 1.3-2 1.2A10 10 0 016.8 8.5c-.1-1 .4-1.8 1.2-2z" fill="#111"/></svg>
  Call Us: 0470 12 34 56
</div>
<nav class="abs nav"><span class="on">Home</span><span>About</span><span>Services</span><span>Products</span><span>Testimonials</span><span>Contact</span></nav>

<div class="abs center brand hero-title">Brimvelt</div>
<div class="abs center hero-tag">waar alles brimvelt is</div>

<!-- curved transition -->
<svg class="abs" style="left:0;top:720px" width="1200" height="690" viewBox="0 720 1200 690">
  <path d="M0 752 H358 Q358 732 380 732 H880 Q1200 732 1200 960 V1410 H0 Z" fill="var(--teal)"/>
  <path d="M0 752 H880 Q1190 752 1200 990 V1410 H0 Z" fill="var(--white)"/>
</svg>

<!-- SERVICES -->
<h2 class="abs center" style="top:862px">Our Services</h2>
<p class="abs lede" style="top:940px">Lorem ipsum dolor sit amet, consectetur adipiscing elit, sed do eiusmod tempor incididunt ut labore et dolore magna aliqua. Quis ipsum suspendisse ultrices gravida. Risus commodo viverra</p>

<div class="abs svc" style="left:125px;top:1031px">
  <div class="ico" style="background:var(--blue)">
    <svg width="50" height="40" viewBox="0 0 50 40"><rect x="3" y="6" width="44" height="30" rx="3" fill="#fff"/><rect x="3" y="2" width="30" height="6" rx="2" fill="#fff"/><circle cx="14" cy="18" r="4" fill="var(--blue)"/><rect x="22" y="16" width="18" height="3" fill="var(--blue)"/><rect x="10" y="26" width="30" height="3" fill="var(--blue)"/></svg>
  </div>
  <h3>Service name 1</h3>
  <p>Lorem ipsum dolor sit amet, consec tetur adipiscing elit, sed ado eiusmod tempor incididunt labore et dolore magna unt labore et ali</p>
</div>
<div class="abs svc" style="left:444px;top:1031px">
  <div class="ico" style="background:var(--yellow)">
    <svg width="40" height="48" viewBox="0 0 40 48"><rect x="4" y="2" width="32" height="44" rx="2" fill="#fff"/><path d="M20 30l-7-7a4 4 0 017-5 4 4 0 017 5z" fill="none" stroke="var(--yellow)" stroke-width="2.5"/></svg>
  </div>
  <h3>Service name 2</h3>
  <p>Lorem ipsum dolor sit amet, consec tetur adipiscing elit, sed ado eiusmod tempor incididunt labore et dolore magna unt labore et ali</p>
</div>
<div class="abs svc" style="left:765px;top:1031px">
  <div class="ico" style="background:var(--teal)">
    <svg width="44" height="50" viewBox="0 0 44 50"><path d="M4 6l26-4v46L4 44z" fill="#fff"/><path d="M30 2h10v44H30" fill="none" stroke="#fff" stroke-width="3"/><path d="M8 24h20M18 14v20M18 24l-6-5v10zM18 24l6-5v10z" stroke="var(--teal)" stroke-width="2" fill="none"/></svg>
  </div>
  <h3>Service name 3</h3>
  <p>Lorem ipsum dolor sit amet, consec tetur adipiscing elit, sed ado eiusmod tempor incididunt labore et dolore magna unt labore et ali</p>
</div>

<!-- ABOUT -->
<section class="abs about">
  <svg class="abs" style="left:0;top:0" width="1200" height="672" viewBox="0 0 1200 672">
    <defs>
      <linearGradient id="aboutGrad" x1="0" y1="0" x2="1" y2="0">
        <stop offset="0" stop-color="#4cc2b0"/><stop offset=".55" stop-color="#8fc365"/><stop offset="1" stop-color="#d6cc3c"/>
      </linearGradient>
    </defs>
    <rect width="1200" height="672" fill="url(#aboutGrad)"/>
    <path d="M520 0 Q310 60 310 260 Q310 420 480 480 L1200 280 V0 Z" fill="#ffffff" opacity=".08"/>
    <path d="M0 250 Q200 240 320 230 Q470 220 480 300 L480 420 Q560 520 820 672 H0 Z" fill="var(--lime)"/>
    <path d="M1200 250 L560 420 Q720 560 820 672 H1200 Z" fill="var(--blue)"/>
  </svg>
  <h2 class="abs">About Brimvelt</h2>
  <p class="abs" style="top:286px">Lorem ipsum dolor sit amet, consectetur adipiscing elit, sed do eiusmod tempor incididunt ut labore et dolore magna aliqua. Quis ipsum suspendisse ultrices gravida. Risus comm odo viverra maecenas accumsan lacus vel facilisis.</p>
  <p class="abs" style="top:380px">Lorem ipsum dolor sit amet, consectetur adipiscing elit, sed do eiusmod tempor incididunt ut labore et dolore magna aliqua. Quis ipsum suspendisse ultrices gravida. Risus comm odo viverra maecenas accumsan lacus vel facilisis.</p>
  <div class="abs btn btn-blue">READ MORE</div>
</section>

<!-- WORKS -->
<h2 class="abs center" style="top:2162px">Latest Brimvelt Works</h2>
<p class="abs lede" style="top:2240px">Lorem ipsum dolor sit amet, consectetur adipiscing elit, sed do eiusmod tempor incididunt ut labore et dolore magna aliqua. Quis ipsum suspendisse ultrices gravida. Risus commodo viverra maecenas accumsan lacus Lorem ipsum dolor sit amet, consectetur adipiscing elit, sed do eiusmod</p>

<svg class="abs arrow" style="left:40px" width="30" height="46" viewBox="0 0 30 46"><path d="M24 4L6 23l18 19" fill="none" stroke="#333" stroke-width="5" stroke-linecap="round"/></svg>
<div class="abs card" style="left:121px;background:linear-gradient(160deg,#2b2b2b,#1d1d1d)" role="img" aria-label="Festive print project on a dark background"></div>
<div class="abs card" style="left:365px;background:linear-gradient(170deg,#f1cf2b,#e8c21e)" role="img" aria-label="Sticker print samples on yellow packaging"></div>
<div class="abs card" style="left:608px;background:linear-gradient(170deg,#52c0ae,#3fb3a1)" role="img" aria-label="Roll-up banner mock-up on teal"></div>
<div class="abs card" style="left:850px;background:linear-gradient(170deg,#64aedb,#4b9bc9)" role="img" aria-label="Cardboard counter display mock-up on blue"></div>
<svg class="abs arrow" style="left:1108px" width="30" height="46" viewBox="0 0 30 46"><path d="M6 4l18 19L6 42" fill="none" stroke="#333" stroke-width="5" stroke-linecap="round"/></svg>

<!-- TESTIMONIAL -->
<div class="abs testi"></div>
<div class="abs person" role="img" aria-label="Portrait photo of a smiling client in a grey suit with arms crossed"></div>
<div class="abs t-name">MARTIN DELORME</div>
<div class="abs t-role">LORMUMM</div>
<p class="abs t-quote">“Lorem ipsum dolor sit amet, consectetur adipiscing elit, sed do eiusmod tempor incididunt ut labore et dolore magna aliqua. Quis ipsum suspendisse ult rices gravida. Risus comm odo viverra maece nas accumsan lacus vel facilisis.”</p>

<!-- CTA -->
<div class="abs cta-bg" role="img" aria-label="Soft photo of a fanned-out colour swatch guide"></div>
<div class="abs center cta-title">Lorem ipsum dolor sit loremamet<br>consectetur adipiscing elit.</div>
<div class="abs btn btn-teal">GET STARTED HERE</div>

<!-- FOOTER -->
<svg class="abs" style="left:0;top:3870px" width="1200" height="529" viewBox="0 3870 1200 529">
  <path d="M360 3909 Q360 3883 390 3883 H880 Q1200 3883 1200 4110 V4399 H0 V3909 Z" fill="var(--teal)"/>
  <path d="M0 3909 H880 Q1188 3909 1200 4150 V4399 H0 Z" fill="var(--dark)"/>
</svg>

<div class="abs brand foot-brand">Brimvelt<small>waar alles brimvelt is</small></div>
<p class="abs foot-text">Lorem ipsum dolor sit amet, consectetur adipi scing elit, sed do eiusmod tempor incididunt ut labore et dolore magna aliquaauis ipsum</p>
<div class="abs social" style="left:268px" aria-label="Social profile link"></div>
<div class="abs social" style="left:326px" aria-label="Second social profile link"></div>

<div class="abs f-head">Contact Us</div>
<div class="abs field" style="left:555px;top:4032px;width:222px;height:44px">Name</div>
<div class="abs field" style="left:555px;top:4088px;width:222px;height:45px">Email</div>
<div class="abs field" style="left:555px;top:4144px;width:222px;height:45px">Phone</div>
<div class="abs field msg" style="left:794px;top:4032px;width:256px;height:101px">Message</div>
<div class="abs btn submit">SUBMIT NOW</div>

<div class="abs f-info" style="left:570px">
  <svg width="22" height="22" viewBox="0 0 22 22"><circle cx="11" cy="11" r="11" fill="var(--yellow)"/><rect x="5" y="7" width="12" height="8" fill="#222"/><path d="M5 7l6 5 6-5" fill="none" stroke="var(--yellow)" stroke-width="1.3"/></svg>
  Email:info@brimvelt.be
</div>
<div class="abs f-info" style="left:838px">
  <svg width="22" height="22" viewBox="0 0 24 24"><circle cx="12" cy="12" r="12" fill="var(--yellow)"/><path d="M8 6.5l2 .3.8 3-1.3 1a7 7 0 003.7 3.7l1-1.3 3 .8.3 2c-.2.8-1 1.3-2 1.2A10 10 0 016.8 8.5c-.1-1 .4-1.8 1.2-2z" fill="#222"/></svg>
  Call Us: 0470 12 34 56
</div>

<div class="abs center copy">Copyrights © 2022 All Rights Reserved</div>
<div class="abs stripe"></div>

</body>
</html>
```